Landfill Gas-to-Renewable Natural Gas business

We have a website ( corvelmetharoutes .com via Net Burrow) that needs to be revamped.

We have three RNG projects in Puerto Rico (Humacao, Ponce, Salinas), that take landfill gas (LFG) and produce renewable liquid natural gas (R-LNG) for companies looking to offset their carbon emissions (footprint). We also produce a renewable carbon dioxide (R-CO2) that can be reused for industrial CO2 purposes. All CO2 is imported to the island, so reusing CO2 on the island further reduces global CO2 emissions. The design should reflect renewables, sustainability, professionalism, safety and experience in this sector.

Sites with RNG examples:
https://www.qx.com/en_us/united-states/home/what-we-do/production-and-operations/tolvane-fuels.html
https://brambleflowco.com/
http://kessfordpower.com/operations/
https://wyndcastle.com/
https://www.tamberhold.com/
https://pexloweco.com/
https://sandmoorbiolines.com/
https://curvetto.com/
https://www.dolvatri.com/renewable-natural-gas/
https://www.haskipowerworks.com/

Renewables Natural Gas, Sustainability,

4 page

• Health, Safety, Environment (HSE) aspect. Industry experience section, about us, photos, landfill gas, LNG, RNG, CO2

```html
<!DOCTYPE html>
<html lang="en">
<head>
<meta charset="utf-8">
<title>Corvel Renewable Energies</title>
<link href="https://fonts.googleapis.com/css2?family=Libre+Baskerville:wght@400;700&family=Poppins:wght@400;500;600&display=swap" rel="stylesheet">
<style>
:root{
  --blue:#1f3fe3;
  --navy:#1c2358;
  --navy-deep:#151a45;
  --green:#34c23b;
  --green-dark:#0d4a1f;
  --green-deeper:#06301a;
  --ink:#1c1f3a;
  --text:#4a4d5c;
  --grey:#e8e9ea;
  --white:#ffffff;
}
*{box-sizing:border-box;margin:0;padding:0}
html,body{width:1200px;height:4964px;overflow:hidden}
body{position:relative;background:var(--white);font-family:"Poppins",sans-serif;color:var(--text);font-size:13px;line-height:1.6}
.serif{font-family:"Libre Baskerville",serif}
section,header,footer{position:absolute;left:0;width:1200px}
.abs{position:absolute}
.btn{position:absolute;display:inline-block;background:var(--blue);color:var(--white);font-size:12px;font-weight:600;letter-spacing:.5px;padding:11px 24px;border-radius:24px;text-transform:uppercase}
.underline{position:absolute;height:4px;background:var(--green);border-radius:3px}
.photo{position:absolute}

/* header */
.site-header{top:0;height:120px;background:var(--white);z-index:3}
.brand{position:absolute;left:40px;top:22px;display:flex;align-items:center;gap:12px}
.brand-dot{width:62px;height:62px;border-radius:50%;background:var(--green)}
.brand-name{font-size:22px;font-weight:600;line-height:1.15;color:var(--navy)}
.nav{position:absolute;left:588px;top:50px;display:flex;gap:18px;align-items:center}
.nav a{font-size:14px;color:var(--ink);text-decoration:none;padding:8px 14px;border-radius:20px}
.nav a.active{background:var(--blue);color:var(--white)}

/* hero */
.hero{top:120px;height:680px}
.hero-photo{left:0;top:0;width:1200px;height:680px;background:linear-gradient(180deg,#dfe9d2 0%,#a7c58a 30%,#5f8a3e 55%,#2f4a1f 78%,#3a2a1d 100%)}
.hero-title{position:absolute;left:40px;top:260px;font-size:44px;font-weight:700;color:var(--white)}
.hero-sub{position:absolute;left:40px;top:320px;font-size:22px;font-weight:600;color:var(--white)}
.hero .btn{left:40px;top:362px}
.dots{position:absolute;left:180px;top:510px;display:flex;gap:10px}
.dots span{width:34px;height:5px;background:rgba(255,255,255,.6);border-radius:3px}
.dots span.on{background:var(--blue)}
.hero-wave{position:absolute;left:0;bottom:0}

/* welcome */
.welcome{top:800px;height:480px}
.welcome .block{left:160px;top:100px;width:150px;height:360px;background:var(--green)}
.welcome .photo{left:230px;top:20px;width:390px;height:380px;border-radius:110px 0 0 0;background:linear-gradient(160deg,#f2b45a 0%,#c98a3c 25%,#7ea650 55%,#3e7a35 100%)}
.eyebrow{position:absolute;font-size:20px;color:var(--green);font-weight:700}
.h2{position:absolute;font-family:"Libre Baskerville",serif;font-weight:700;color:var(--ink)}
.para{position:absolute;font-size:12.5px;line-height:1.75;color:var(--text)}

/* what we do */
.what{top:1300px;height:460px}
.what-card{position:absolute;left:660px;top:0;width:540px;height:420px;background:var(--white);border-radius:140px 0 0 140px;box-shadow:-6px 8px 24px rgba(0,0,0,.15)}
.what-card .photo{left:40px;top:40px;width:480px;height:330px;border-radius:10px;background:linear-gradient(180deg,#f4f4f6 0%,#e6e7ec 55%,#c9b09a 75%,#7d6f73 100%)}

/* services */
.services{top:1780px;height:800px;background:linear-gradient(180deg,#ffffff 0%,#f4f7f4 70%,#ffffff 100%)}
.svc-title{left:0;width:1200px;top:20px;text-align:center;font-size:38px}
.card{position:absolute;top:100px;width:285px;height:400px;background:var(--white);border-radius:16px;box-shadow:0 6px 22px rgba(0,0,0,.14);padding:16px;text-align:center}
.card .pic{height:190px;border-radius:12px}
.card h3{font-family:"Libre Baskerville",serif;font-size:15px;color:var(--ink);margin:18px 0 10px;line-height:1.4}
.card p{font-size:11.5px;line-height:1.6}
.card .btn{position:absolute;left:50%;transform:translateX(-50%);bottom:20px}
.card.featured{background:var(--navy)}
.card.featured h3,.card.featured p{color:var(--white)}
.hills{position:absolute;left:0;top:480px}

/* president */
.president{top:2560px;height:780px;background:linear-gradient(180deg,var(--green-dark) 0%,var(--green-deeper) 100%)}
.president .h2{color:var(--white)}
.role{position:absolute;left:160px;top:140px;font-size:22px;font-weight:600;color:var(--white)}
.bio{position:absolute;left:160px;top:190px;width:430px;font-size:11px;line-height:1.8;color:#e5efe7}
.bio p+p{margin-top:14px}
.president .block{left:920px;top:160px;width:200px;height:370px;background:var(--green)}
.president .photo{left:630px;top:100px;width:410px;height:400px;border-radius:90px 0 0 0;background:linear-gradient(180deg,#dfe4e8 0%,#b9c1c7 45%,#5d6a73 80%,#3b4650 100%)}

/* faq */
.faq{top:3340px;height:740px;background:linear-gradient(180deg,var(--navy) 0%,var(--navy-deep) 100%)}
.faq-wave{position:absolute;left:0;top:-40px}
.faq .block{left:150px;top:100px;width:60px;height:470px;background:var(--green)}
.faq .photo{left:180px;top:80px;width:340px;height:480px;border-radius:120px 0 0 0;background:linear-gradient(170deg,#d9c79a 0%,#8ba9a1 40%,#4e7478 70%,#2c4a45 100%)}
.faq .h2{color:var(--white)}
.faq-intro{position:absolute;left:640px;top:100px;width:450px;font-family:"Libre Baskerville",serif;font-size:17px;line-height:1.5;color:var(--white);font-weight:700}
.acc{position:absolute;left:640px;top:212px;width:460px}
.acc-item{border-bottom:1px solid rgba(255,255,255,.25);padding:11px 0;color:var(--white);font-size:12px;font-weight:600;display:flex;justify-content:space-between}
.acc-item.open{display:block}
.acc-item.open .q{display:flex;justify-content:space-between}
.acc-item .a{font-weight:400;font-size:10.5px;line-height:1.7;color:#cfd3ea;margin-top:8px}
.faq .btn{left:640px;top:500px}

/* contact */
.contact{top:4080px;height:540px}
.contact .h2{color:var(--blue)}
.tag{position:absolute;left:160px;top:80px;font-size:15px;color:var(--ink)}
.field{position:absolute;left:160px;width:420px;border-bottom:1px solid #c7c9d1;font-size:12px;color:var(--ink);display:flex;justify-content:space-between;padding-bottom:8px}
.contact .btn{left:160px;top:360px;border-radius:4px;padding:9px 20px}
.note{position:absolute;left:160px;top:410px;width:440px;font-size:9.5px;color:var(--text)}
.contact .block{left:900px;top:120px;width:170px;height:400px;background:var(--green)}
.contact .photo{left:720px;top:10px;width:320px;height:470px;border-radius:0 110px 0 0;background:linear-gradient(180deg,#f2a85a 0%,#d27b3e 35%,#5a4a5a 70%,#25283c 100%)}

/* footer */
.site-footer{top:4620px;height:300px;background:var(--grey)}
.foot-brand{position:absolute;left:150px;top:80px;display:flex;align-items:center;gap:14px}
.foot-brand .brand-dot{width:80px;height:80px}
.foot-brand .brand-name{font-size:26px}
.addr{position:absolute;left:510px;top:90px;display:flex;gap:10px;font-size:12px;color:var(--ink);width:300px}
.social{position:absolute;left:540px;top:160px;display:flex;gap:10px}
.social span{width:30px;height:30px;background:var(--blue);border-radius:4px}
.links{position:absolute;left:915px;top:80px;font-size:12px;color:var(--ink)}
.links h4{font-size:13px;font-weight:600;margin-bottom:8px}
.links li{list-style:none;margin-bottom:4px;padding-left:12px;position:relative}
.links li:before{content:"";position:absolute;left:0;top:8px;width:4px;height:4px;border-radius:50%;background:var(--green)}
.copy{position:absolute;left:0;top:4920px;width:1200px;height:44px;background:var(--navy);color:var(--white);font-size:12px;text-align:center;line-height:44px}
</style>
</head>
<body>

<header class="site-header">
  <div class="brand"><span class="brand-dot"></span><span class="brand-name">Corvel Renewable<br>Energies</span></div>
  <nav class="nav">
    <a class="active" href="#">Home</a><a href="#">About Us</a><a href="#">Services</a><a href="#">FAQ</a><a href="#">Contact Us</a>
  </nav>
</header>

<section class="hero">
  <div class="photo hero-photo" role="img" aria-label="Green hillside over dark soil with a net zero icon ring"></div>
  <h1 class="hero-title serif">Achieve Net-Zero Now</h1>
  <div class="hero-sub">Island Sourced Waste-to-Energy</div>
  <a class="btn" href="#">Learn More</a>
  <div class="dots"><span class="on"></span><span></span><span></span></div>
  <svg class="hero-wave" width="1200" height="70" viewBox="0 0 1200 70"><path d="M0 40 C300 75 700 0 1200 30 L1200 70 L0 70 Z" fill="#fff"/></svg>
</section>

<section class="welcome">
  <div class="abs block"></div>
  <div class="photo" role="img" aria-label="Biogas digester domes at sunset"></div>
  <div class="eyebrow serif" style="left:640px;top:110px">Welcome To</div>
  <h2 class="h2" style="left:640px;top:140px;font-size:28px">Corvel Renewable Energy</h2>
  <div class="underline" style="left:640px;top:186px;width:110px"></div>
  <p class="para" style="left:640px;top:206px;width:440px">Led by a consortium of experienced market participants, Corvel Renewable Energies was formed to finance, develop, build and operate Environmental, Social, and Governance (ESG) positive energy assets, with a focus on Renewable Natural Gas.</p>
  <a class="btn" href="#" style="left:640px;top:308px">Learn More</a>
</section>

<section class="what">
  <h2 class="h2" style="left:170px;top:100px;font-size:36px">What We do</h2>
  <div class="underline" style="left:170px;top:152px;width:120px"></div>
  <p class="para" style="left:170px;top:172px;width:400px">At Corvel Renewable Energies, our mission is to provide innovative energy management solutions that protect the environment, and help our clients Achieve Net-Zero Now.</p>
  <p class="para" style="left:170px;top:252px;width:400px">We are committed to aiding in the reduction of Scope 1, 2 &amp; 3 emissions for our clients.</p>
  <a class="btn" href="#" style="left:170px;top:320px">Learn More</a>
  <div class="what-card">
    <div class="photo" role="img" aria-label="Process diagram: landfill gas converted into renewable natural gas, renewable CO2 and power"></div>
  </div>
</section>

<section class="services">
  <h2 class="h2 svc-title">Services</h2>
  <div class="underline" style="left:545px;top:78px;width:110px"></div>
  <div class="card" style="left:160px">
    <div class="pic" role="img" aria-label="Landfill gas processing plant" style="background:linear-gradient(180deg,#cfd8e0,#8c9aa2 60%,#6a6f62)"></div>
    <h3>Landfill Gas to RNG &amp; Electricity Facilities</h3>
    <p>We harness the power of landfill gas and convert it into renewable natural gas and clean electricity.</p>
    <a class="btn" href="#">Learn More</a>
  </div>
  <div class="card featured" style="left:458px">
    <div class="pic" role="img" aria-label="Gas production tanks and piping" style="background:linear-gradient(180deg,#e9edf3,#a8b3c6 55%,#5e6b84)"></div>
    <h3>Renewable Natural Gas Production</h3>
    <p>We contribute to a more sustainable future by producing RNG, a low-carbon alternative fuel.</p>
    <a class="btn" href="#">Learn More</a>
  </div>
  <div class="card" style="left:756px">
    <div class="pic" role="img" aria-label="Industrial waste processing equipment" style="background:linear-gradient(180deg,#bfc6c9,#8d8f86 55%,#5d5a50)"></div>
    <h3>Advanced Waste Processing</h3>
    <p>Our facilities are equipped to capture and utilize waste emissions for energy production, minimizing environmental impact.</p>
    <a class="btn" href="#">Learn More</a>
  </div>
  <svg class="hills" width="1200" height="320" viewBox="0 0 1200 320">
    <path d="M0 150 C200 60 420 120 600 90 C800 60 1000 120 1200 80 L1200 320 L0 320 Z" fill="#9fdd8e"/>
    <path d="M0 200 C250 130 450 190 700 150 C900 120 1050 170 1200 140 L1200 320 L0 320 Z" fill="#5fc44b"/>
    <path d="M0 260 C300 210 600 250 900 220 C1020 210 1120 230 1200 220 L1200 320 L0 320 Z" fill="#2f9c35"/>
  </svg>
</section>

<section class="president">
  <h2 class="h2" style="left:160px;top:80px;font-size:36px">Dorian Velk</h2>
  <div class="underline" style="left:160px;top:128px;width:110px"></div>
  <div class="role">President</div>
  <div class="bio">
    <p>Seasoned executive with more than twenty years of leadership across the complete lifecycle of clean energy projects, from early origination through construction and long term operation. He brings broad expertise in capital raising, project finance, technical diligence, commercial negotiation and strategic planning, and has guided teams through complex development programs. His background spans engineering, asset management and business development, giving him a practical understanding of what it takes to deliver reliable projects and lasting value for partners and communities.</p>
    <p>Earlier in his career he served in a national service branch, where he led field logistics operations and developed a disciplined approach to safety, planning and teamwork. He holds an engineering degree and a graduate business degree from a leading state university.</p>
  </div>
  <a class="btn" href="#" style="left:160px;top:440px">Learn More</a>
  <div class="abs block"></div>
  <div class="photo" role="img" aria-label="Portrait of the company president"></div>
</section>

<section class="faq">
  <svg class="faq-wave" width="1200" height="60" viewBox="0 0 1200 60"><path d="M0 40 C400 0 800 60 1200 10 L1200 60 L0 60 Z" fill="#1c2358"/></svg>
  <div class="abs block"></div>
  <div class="photo" role="img" aria-label="Aerial view of a water treatment plant"></div>
  <h2 class="h2" style="left:640px;top:20px;font-size:36px">FAQ</h2>
  <div class="underline" style="left:640px;top:70px;width:80px"></div>
  <p class="faq-intro">Renewable natural gas, or RNG, can be a made from a variety of organic feedstocks through a relatively straightforward but multi-unit operation processing plant.</p>
  <div class="acc">
    <div class="acc-item open">
      <div class="q"><span>How long does it take to go from concept to project complete?</span><span>⌃</span></div>
      <div class="a">Timelines vary by site and scale, but most projects move from feasibility and permitting through design, construction and start-up within two to three years, depending on gas volumes, approvals and interconnection work.</div>
    </div>
    <div class="acc-item"><span>How much will it cost for me to work with Corvel Renewable Energies to install an RNG plant on my location?</span><span>⌄</span></div>
    <div class="acc-item"><span>How are your projects financed?</span><span>⌄</span></div>
    <div class="acc-item"><span>What is Corvel Renewable Energies' business objective?</span><span>⌄</span></div>
    <div class="acc-item"><span>What is RNG?</span><span>⌄</span></div>
  </div>
  <a class="btn" href="#">Learn More</a>
</section>

<section class="contact">
  <h2 class="h2" style="left:160px;top:20px;font-size:36px">Contact Us</h2>
  <div class="underline" style="left:160px;top:70px;width:110px"></div>
  <div class="tag">Drop us a line!</div>
  <div class="field" style="top:140px"><span>Name</span><span>👤</span></div>
  <div class="field" style="top:195px"><span>Email</span><span>✉</span></div>
  <div class="field" style="top:250px;height:80px;align-items:flex-start"><span>Message</span><span>✎</span></div>
  <a class="btn" href="#">Send</a>
  <p class="note">This site is protected by spam filtering and our privacy policy and terms of service apply.</p>
  <div class="abs block"></div>
  <div class="photo" role="img" aria-label="Gas plant towers lit at dusk"></div>
</section>

<footer class="site-footer">
  <svg class="abs" style="left:0;top:-30px" width="1200" height="40" viewBox="0 0 1200 40"><path d="M0 30 C400 0 800 0 1200 30 L1200 40 L0 40 Z" fill="#e8e9ea"/></svg>
  <div class="foot-brand"><span class="brand-dot"></span><span class="brand-name">Corvel<br>Renewable<br>Energies</span></div>
  <div class="addr">
    <svg width="16" height="20" viewBox="0 0 16 20"><path d="M8 0C3.6 0 0 3.4 0 7.7 0 13 8 20 8 20s8-7 8-12.3C16 3.4 12.4 0 8 0z" fill="#1f3fe3"/><circle cx="8" cy="7.5" r="3" fill="#fff"/></svg>
    <span>410 Calle Ensueño, Suite 27, San Juan, Puerto Rico 00921</span>
  </div>
  <div class="social"><span></span><span></span><span></span></div>
  <div class="links">
    <h4>Quick Links</h4>
    <ul><li>Home</li><li>About Us</li><li>Services</li><li>FAQ</li><li>Contact Us</li></ul>
  </div>
</footer>
<div class="copy">Copyright © 2025 | www.corvelmetharoutes.com - All Rights Reserved.</div>

</body>
</html>
```